Bramworth email header for parts

We sell parts to the construction equipment industry. We want a header for our emails that reflect what we do. I will include what we have now but want something for parts only. Added a lot of pictures just so you can look through what we do.

```html
<!DOCTYPE html>
<html lang="en">
<head>
<meta charset="utf-8">
<title>Bramworth Parts Email Headers</title>
<link rel="stylesheet" href="https://fonts.googleapis.com/css2?family=Russo+One&family=Teko:wght@400&display=swap">
<style>
  :root {
    --page: #f0f0f0;
    --banner-dark: #1c1c1e;
    --banner-mid: #333336;
    --brand-red: #e3161b;
    --white: #ffffff;
  }
  * { margin: 0; padding: 0; box-sizing: border-box; }
  html, body { width: 1200px; height: 1131px; overflow: hidden; background: var(--page); }
  .canvas { position: relative; width: 1200px; height: 1131px; }

  .header-banner {
    position: absolute;
    left: 75px;
    width: 1048px;
    height: 322px;
    overflow: hidden;
    background: radial-gradient(ellipse at 40% 45%, var(--banner-mid) 0%, var(--banner-dark) 75%);
    font-family: "Russo One", sans-serif;
  }
  .banner-one { top: 54px; }
  .banner-two { top: 402px; }
  .banner-three { top: 750px; }

  .banner-art { position: absolute; inset: 0; width: 1048px; height: 322px; }

  .brand-name {
    position: absolute;
    left: 195px;
    top: 82px;
    width: 160px;
    display: flex;
    align-items: center;
    justify-content: center;
    gap: 7px;
    color: var(--white);
    font-size: 17px;
    letter-spacing: 0.5px;
  }
  .brand-mark { width: 12px; height: 12px; background: var(--brand-red); }

  .headline-tanks {
    position: absolute;
    left: 60px;
    top: 126px;
    width: 426px;
    text-align: center;
    color: var(--brand-red);
    font-family: "Teko", sans-serif;
    font-weight: 400;
    font-size: 50px;
    line-height: 48px;
    white-space: nowrap;
  }
  .headline-parts {
    position: absolute;
    left: 60px;
    top: 174px;
    width: 426px;
    text-align: center;
    color: var(--white);
    font-size: 37px;
    line-height: 48px;
    white-space: nowrap;
    text-shadow: 0 3px 4px rgba(0,0,0,0.6);
  }
  .phone-line {
    position: absolute;
    left: 60px;
    top: 251px;
    height: 71px;
    display: flex;
    align-items: center;
    gap: 30px;
    color: var(--white);
    font-size: 40px;
    letter-spacing: 0.5px;
    white-space: nowrap;
  }
  .phone-icon { width: 32px; height: 32px; }
</style>
</head>
<body>
<div class="canvas">

  <section class="header-banner banner-one">
    <svg class="banner-art" viewBox="0 0 1048 322">
      <defs>
        <linearGradient id="partsDark" x1="0" y1="0" x2="1" y2="1">
          <stop offset="0" stop-color="#3a3a3a"/><stop offset="1" stop-color="#0d0d0d"/>
        </linearGradient>
        <linearGradient id="partsYellow" x1="0" y1="0" x2="1" y2="1">
          <stop offset="0" stop-color="#f5d23a"/><stop offset="1" stop-color="#c99a10"/>
        </linearGradient>
      </defs>
      <polygon points="0,251 520,251 556,322 0,322" fill="var(--brand-red)"/>
      <circle cx="578" cy="82" r="67" fill="var(--brand-red)" stroke="#fff" stroke-width="4"/>
      <circle cx="578" cy="82" r="48" fill="url(#partsDark)" role="img" aria-label="Final drive sprocket part"/>
      <circle cx="795" cy="82" r="67" fill="var(--brand-red)" stroke="#fff" stroke-width="4"/>
      <circle cx="795" cy="82" r="48" fill="url(#partsDark)" role="img" aria-label="Idler wheel and segment ring parts"/>
      <circle cx="676" cy="230" r="67" fill="var(--brand-red)" stroke="#fff" stroke-width="4"/>
      <circle cx="676" cy="230" r="50" fill="url(#partsYellow)" role="img" aria-label="Yellow steering knuckle part"/>
      <circle cx="910" cy="230" r="67" fill="var(--brand-red)" stroke="#fff" stroke-width="4"/>
      <circle cx="910" cy="230" r="50" fill="url(#partsYellow)" role="img" aria-label="Yellow transmission housing part"/>
    </svg>
    <div class="brand-name"><span class="brand-mark"></span>BRAMWORTH</div>
    <div class="headline-tanks">CUSTOM BUILT WATER TANKS</div>
    <div class="headline-parts">REPLACEMENT PARTS</div>
    <div class="phone-line">
      <svg class="phone-icon" viewBox="0 0 24 24"><path fill="#fff" d="M6.6 10.8a15.1 15.1 0 0 0 6.6 6.6l2.2-2.2c.3-.3.7-.4 1-.2 1.1.4 2.3.6 3.6.6.6 0 1 .4 1 1V20c0 .6-.4 1-1 1A17 17 0 0 1 3 4c0-.6.4-1 1-1h3.5c.6 0 1 .4 1 1 0 1.3.2 2.5.6 3.6.1.3 0 .7-.2 1z"/></svg>
      <span class="phone-number">555 014 2700</span>
    </div>
  </section>

  <section class="header-banner banner-two">
    <svg class="banner-art" viewBox="0 0 1048 322">
      <defs>
        <linearGradient id="partsGroup" x1="0" y1="0" x2="1" y2="0">
          <stop offset="0" stop-color="#151515"/><stop offset="0.4" stop-color="#2a2a2a"/>
          <stop offset="0.55" stop-color="#e8b816"/><stop offset="1" stop-color="#f2c21a"/>
        </linearGradient>
      </defs>
      <polygon points="0,251 520,251 556,322 0,322" fill="var(--brand-red)"/>
      <rect x="505" y="12" width="516" height="300" rx="60" fill="url(#partsGroup)" role="img" aria-label="Group of heavy equipment parts: sprockets, idler, steering knuckle and yellow transmission housing"/>
    </svg>
    <div class="brand-name"><span class="brand-mark"></span>BRAMWORTH</div>
    <div class="headline-tanks">CUSTOM BUILT WATER TANKS</div>
    <div class="headline-parts">REPLACEMENT PARTS</div>
    <div class="phone-line">
      <svg class="phone-icon" viewBox="0 0 24 24"><path fill="#fff" d="M6.6 10.8a15.1 15.1 0 0 0 6.6 6.6l2.2-2.2c.3-.3.7-.4 1-.2 1.1.4 2.3.6 3.6.6.6 0 1 .4 1 1V20c0 .6-.4 1-1 1A17 17 0 0 1 3 4c0-.6.4-1 1-1h3.5c.6 0 1 .4 1 1 0 1.3.2 2.5.6 3.6.1.3 0 .7-.2 1z"/></svg>
      <span class="phone-number">555 014 2700</span>
    </div>
  </section>

  <section class="header-banner banner-three">
    <svg class="banner-art" viewBox="0 0 1048 322">
      <defs>
        <linearGradient id="tankYellow" x1="0" y1="0" x2="0" y2="1">
          <stop offset="0" stop-color="#f7c62a"/><stop offset="1" stop-color="#d99d12"/>
        </linearGradient>
      </defs>
      <polygon points="0,251 520,251 556,322 0,322" fill="var(--brand-red)"/>
      <rect x="540" y="100" width="448" height="190" rx="40" fill="url(#tankYellow)" role="img" aria-label="Yellow custom built water tanker tank"/>
    </svg>
    <div class="brand-name"><span class="brand-mark"></span>BRAMWORTH</div>
    <div class="headline-tanks">CUSTOM BUILT WATER TANKS</div>
    <div class="headline-parts">REPLACEMENT PARTS</div>
    <div class="phone-line">
      <svg class="phone-icon" viewBox="0 0 24 24"><path fill="#fff" d="M6.6 10.8a15.1 15.1 0 0 0 6.6 6.6l2.2-2.2c.3-.3.7-.4 1-.2 1.1.4 2.3.6 3.6.6.6 0 1 .4 1 1V20c0 .6-.4 1-1 1A17 17 0 0 1 3 4c0-.6.4-1 1-1h3.5c.6 0 1 .4 1 1 0 1.3.2 2.5.6 3.6.1.3 0 .7-.2 1z"/></svg>
      <span class="phone-number">555 014 2700</span>
    </div>
  </section>

</div>
</body>
</html>
```